Letterhead for a Natural Hair Run

We need a letterhead design with the logo uploaded entitled 'Bluevista Dash'. This run is a natural 5K run seeking to promote the acceptance of natural beauty in every aspect of society encompassing one's ethnic roots and its connection to a healthy lifetstyle. We would like to see designs coordinating with our logo. The design should be fun and exciting!

Industry/Entity Type

Hair

Font styles to use
Serif
Sans Serif

Requirements
Must have
• Please included this information on the letter head:
• P.O. Box K7214
• Port Linden, Calder Isles
• Phone: (318) 618-2097
• Email: goskyward517@mailbrisk.net

```html
<!DOCTYPE html>
<html lang="en">
<head>
<meta charset="utf-8">
<title>Bluevista Dash — Stationery</title>
<link href="https://fonts.googleapis.com/css2?family=Lato:wght@400;700&display=swap" rel="stylesheet">
<style>
  :root {
    --backdrop: #151515;
    --paper: #ffffff;
    --brand-cyan: #03b6d4;
    --ink: #444444;
    --ink-soft: #666666;
    --ink-dark: #111111;
    --label-yellow: #f4e04d;
    --rule: #eeeeee;
  }
  * { margin: 0; padding: 0; box-sizing: border-box; }
  html, body { width: 1200px; height: 1001px; overflow: hidden; background: var(--backdrop); }
  body { position: relative; font-family: "Lato", sans-serif; color: var(--ink); }

  .brand-name { font-family: "Lato", sans-serif; font-weight: 400; white-space: nowrap; }

  /* Letterhead */
  .letterhead { position: absolute; left: 120px; top: 141px; width: 423px; height: 635px; background: var(--paper); }
  .letterhead-header { position: absolute; left: 0; top: 0; width: 100%; height: 65px; border-bottom: 1px solid var(--rule); }
  .letterhead-header .brand-name { position: absolute; left: 0; width: 100%; top: 40px; text-align: center; font-size: 12px; color: var(--ink-dark); }
  .recipient { position: absolute; left: 34px; top: 108px; font-size: 8.8px; line-height: 14.8px; color: var(--ink); font-style: normal; }
  .recipient .recipient-name { font-weight: 700; }
  .salutation { position: absolute; left: 33px; top: 205px; font-size: 10px; font-weight: 700; color: var(--ink); }
  .letter-body { position: absolute; left: 33px; top: 226px; width: 358px; font-size: 6.1px; line-height: 16.2px; color: var(--ink-soft); }
  .letter-body p + p { margin-top: 12.5px; }
  .closing { position: absolute; top: 476px; font-size: 8.6px; color: var(--ink); }
  .closing.left { left: 34px; }
  .closing.right { right: 29px; }
  .signer { position: absolute; left: 33px; top: 497px; font-size: 8.6px; line-height: 16px; color: var(--ink-soft); }

  .letterhead-footer { position: absolute; left: 0; top: 584px; width: 100%; height: 41px; background: var(--brand-cyan); }
  .footer-contact { position: absolute; left: 29px; top: 9px; font-size: 5.6px; line-height: 12px; color: #fff; }
  .footer-contact .label { color: var(--label-yellow); }
  .footer-contact .gap { display: inline-block; width: 26px; }
  .footer-badge { position: absolute; left: 349px; top: -6px; width: 53px; height: 53px; border-radius: 50%; background: var(--paper); display: flex; align-items: center; justify-content: center; }
  .footer-badge .brand-name { font-size: 6px; color: var(--ink-dark); }

  /* Envelope front */
  .envelope-front { position: absolute; left: 608px; top: 190px; width: 489px; height: 245px; background: var(--brand-cyan); }
  .envelope-front .brand-name { position: absolute; left: 0; width: 100%; top: 95px; text-align: center; font-size: 18px; color: #fff; }
  .envelope-front .divider { position: absolute; left: 0; top: 200px; width: 100%; height: 1px; background: rgba(255,255,255,0.35); }
  .envelope-contact { position: absolute; top: 212px; font-size: 6.8px; color: #fff; display: flex; align-items: center; gap: 3px; white-space: nowrap; }
  .envelope-contact svg { width: 7px; height: 7px; fill: #fff; }

  /* Envelope back */
  .envelope-back { position: absolute; left: 609px; top: 482px; width: 500px; height: 250px; background: var(--paper); }
  .envelope-back .flap { position: absolute; left: 0; top: 0; }
  .envelope-back .brand-name { position: absolute; left: 0; width: 100%; top: 212px; text-align: center; font-size: 12px; color: var(--ink-dark); }
</style>
</head>
<body>

<section class="letterhead">
  <header class="letterhead-header">
    <span class="brand-name">Bluevista Dash</span>
  </header>

  <address class="recipient">
    <div class="recipient-name">Jonathan Smith</div>
    <div>Owner</div>
    <div>Company Name</div>
    <div>Address Line1, Address Line2</div>
    <div>Country -123456</div>
  </address>

  <div class="salutation">Dear John Smith</div>

  <div class="letter-body">
    <p>Lorem ipsum dolor sit amet, consectetur adipiscing elit, sed do eiusmod tempor incididunt ut labore et dolore magna aliqua. Ut enim ad minim veniam, quis nostrud exercitation ullamco laboris nisi ut aliquip ex ea commodo consequat. Duis aute irure dolor in reprehenderit in voluptate velit esse cillum dolore eu fugiat nulla pariatur. Excepteur sint occaecat cupidatat non proident, sunt in culpa qui officia deserunt mollit anim id est laborum.</p>
    <p>Lorem ipsum dolor sit amet, consectetur adipiscing elit, sed do eiusmod tempor incididunt ut labore et dolore magna aliqua. Ut enim ad minim veniam, quis nostrud exercitation ullamco laboris nisi ut aliquip ex ea commodo consequat. Duis aute irure dolor in reprehenderit in voluptate velit esse cillum dolore</p>
    <p>Lorem ipsum dolor sit amet, consectetur adipiscing elit, sed do eiusmod tempor incididunt ut labore et dolore magna aliqua. Ut enim ad minim veniam, quis nostrud exercitation ullamco laboris nisi ut aliquip ex ea commodo consequat. Duis aute irure dolor in reprehenderit in voluptate velit esse cillum dolore eu fugiat nulla pariatur. Excepteur sint occaecat cupidatat non proident, sunt in culpa qui officia deserunt mollit anim id est laborum.</p>
  </div>

  <div class="closing left">Sincerely,</div>
  <div class="closing right">Your Faithfully</div>
  <div class="signer">
    <div>[ your Name ]</div>
    <div>[ Title ]</div>
  </div>

  <footer class="letterhead-footer">
    <div class="footer-contact">
      <div><span class="label">Phone:</span> (318) 618-2097<span class="gap"></span><span class="label">Email:</span> goskyward517@mailbrisk.net</div>
      <div><span class="label">Address :</span> P.O. Box K7214 Port Linden, Calder Isles</div>
    </div>
    <div class="footer-badge"><span class="brand-name">Bluevista Dash</span></div>
  </footer>
</section>

<section class="envelope-front">
  <span class="brand-name">Bluevista Dash</span>
  <div class="divider"></div>
  <div class="envelope-contact" style="left:72px">
    <span>(318) 618-2097</span>
    <svg viewBox="0 0 24 24" aria-hidden="true"><path d="M6.6 10.8c1.4 2.8 3.8 5.1 6.6 6.6l2.2-2.2c.3-.3.7-.4 1-.2 1.1.4 2.3.6 3.6.6.6 0 1 .4 1 1V20c0 .6-.4 1-1 1C10.6 21 3 13.4 3 4c0-.6.4-1 1-1h3.5c.6 0 1 .4 1 1 0 1.3.2 2.5.6 3.6.1.3 0 .7-.2 1l-2.3 2.2z"/></svg>
  </div>
  <div class="envelope-contact" style="left:158px">
    <span>goskyward517@mailbrisk.net</span>
    <svg viewBox="0 0 24 24" aria-hidden="true"><path d="M2 5h20v14H2z" opacity=".9"/><path d="M2 5l10 8 10-8" fill="none" stroke="#03b6d4" stroke-width="2"/></svg>
  </div>
  <div class="envelope-contact" style="left:280px">
    <span>P.O. Box K7214 Port Linden, Calder Isles</span>
    <svg viewBox="0 0 24 24" aria-hidden="true"><path d="M12 2a7 7 0 0 0-7 7c0 5 7 13 7 13s7-8 7-13a7 7 0 0 0-7-7zm0 9.5A2.5 2.5 0 1 1 12 6.5a2.5 2.5 0 0 1 0 5z"/></svg>
  </div>
</section>

<section class="envelope-back">
  <svg class="flap" width="500" height="55" viewBox="0 0 500 55" aria-hidden="true">
    <polygon points="0,0 500,0 480,54 20,54" fill="var(--brand-cyan)"/>
  </svg>
  <span class="brand-name">Bluevista Dash</span>
</section>

</body>
</html>
```